Cybersecurity company is looking for business card.

I need a business card design for our company, we are a cybersecurity company providing advance technology to protect agains any kind of malware. We need a fresh modern design it should communicate modern, technology and growth.

Target Market(s)

Business to business

Industry/Entity Type

Business

Contact Information for Business Card

Should have location, address, fax, mobile, phone, email and website.

Requirements
Must have
• Must follow company's logo color and style. Must have the company's log on its.

```html
<!DOCTYPE html>
<html lang="en">
<head>
<meta charset="utf-8">
<title>Vextora Business Card</title>
<link href="https://fonts.googleapis.com/css2?family=Arimo:wght@400;700&display=swap" rel="stylesheet">
<style>
  :root {
    --backdrop: #1e1e1e;
    --card-white: #ffffff;
    --ink-black: #000000;
    --brand-red: #a01d22;
    --text-dark: #111111;
  }
  * { margin: 0; padding: 0; box-sizing: border-box; }
  html, body {
    width: 1200px; height: 800px; overflow: hidden;
    background: var(--backdrop);
    font-family: "Arimo", Arial, sans-serif;
  }
  .stage { position: relative; width: 1200px; height: 800px; }
  .card {
    position: absolute; top: 263px;
    width: 480px; height: 274px;
    background: var(--card-white);
    overflow: hidden;
    box-shadow: 0 6px 18px rgba(0,0,0,0.5);
  }
  .card--front { left: 98px; }
  .card--back { left: 622px; }
  .card__shapes { position: absolute; inset: 0; width: 480px; height: 274px; }

  .wordmark {
    position: absolute;
    font-weight: 700;
    letter-spacing: 1px;
    line-height: 1;
  }
  .card--front .wordmark { left: 186px; top: 160px; font-size: 50px; color: var(--card-white); }
  .card--back .wordmark { left: 28px; top: 54px; font-size: 50px; color: var(--ink-black); }

  .front-url {
    position: absolute; left: 188px; top: 222px;
    font-size: 10px; letter-spacing: 5.2px;
    color: var(--brand-red);
  }

  .address {
    position: absolute; left: 28px; top: 141px;
    font-size: 12px; line-height: 14px; color: var(--text-dark);
    font-style: normal;
  }
  .contacts {
    position: absolute; left: 28px; top: 203px;
    font-size: 12px; line-height: 14px; color: var(--text-dark);
    list-style: none;
  }
  .contacts .label {
    color: var(--brand-red); font-weight: 700; font-size: 9px;
  }
  .online {
    position: absolute; right: 26px; top: 205px;
    text-align: right; color: var(--card-white);
  }
  .online .email { font-size: 13px; font-weight: 700; line-height: 16px; }
  .online .site { font-size: 21px; font-weight: 700; line-height: 28px; }
</style>
</head>
<body>
<main class="stage">
  <section class="card card--front" aria-label="Business card front">
    <svg class="card__shapes" viewBox="0 0 480 274" aria-hidden="true">
      <polygon points="310,0 480,0 480,274 37,274" fill="var(--ink-black)"/>
      <path d="M42,30 H198 Q212,30 204,42 L52,206 Q36,222 32,200 V40 Q32,30 42,30 Z" fill="var(--brand-red)"/>
    </svg>
    <div class="wordmark">vextora</div>
    <div class="front-url">www.vextora.com</div>
  </section>

  <section class="card card--back" aria-label="Business card back">
    <svg class="card__shapes" viewBox="0 0 480 274" aria-hidden="true">
      <polygon points="423,0 480,0 480,274 173,274" fill="var(--brand-red)"/>
    </svg>
    <div class="wordmark">vextora</div>
    <address class="address">
      Harbor Bay - Nordia<br>
      Harbor Tech Park (HTP)<br>
      Meridian Avenue.
    </address>
    <ul class="contacts">
      <li><span class="label">mobile</span> +00 55 123 XXXX</li>
      <li><span class="label">phone</span> 07 123 XXXX</li>
      <li><span class="label">fax</span> 07 123 XXXX</li>
    </ul>
    <div class="online">
      <div class="email">name.surname@vextora.com</div>
      <div class="site">www.vextora.com</div>
    </div>
  </section>
</main>
</body>
</html>
```